Label for natural soft drink / juice

Required is a label design that adds a frame for a range of different labels linked to a variety of tastes for a natural, organic, sparkling beverage in a multi-use, environmentally friendly returnable clear glass bottle.
The 2 first tastes are rhubarb and apple
The label will be a paper label sticked at the front side of the bottle.
No glossy or shiny appearance as it does not fit the organic image
No color restrictions in general, but
Blue better than green
Matt better than glossy
Fit of colours on one label essential, so no “crying colour mixture” (great also: complementary contrasts like blue/orange)
Handpainted better than photorealistic
Simple better than overcrowded
Smart, funny intelligent a lot better than same standard as everywhere
For the image consider subtile reminiscence to the fruit or other stuff linked to the fruit (even “across 3 corners”, so a bit far away) as a nice additional asset

Target Market(s)

modern restaurants with high quality food, often with organic and regional products on the menu.

Font styles to use
Serif
Sans Serif
Script

Requirements
Nice to have
• the fruit of the current taste or something linked to the fruit as e.g. reminiscence to well known story or history of the fruit
Should not have
• too many elements on the label. simplicity is key

```html
<!DOCTYPE html>
<html lang="en">
<head>
<meta charset="utf-8">
<title>Waldhorn – Apple label</title>
<link rel="stylesheet" href="https://fonts.googleapis.com/css2?family=Oswald:wght@300;400;700&display=swap">
<style>
  :root {
    --label-yellow: #f2df82;
    --label-cream: #efdcaa;
    --wave-shadow: #e4c07c;
    --frame-gold: #d6a42a;
    --ink: #16162a;
    --art-red: #d8432e;
    --art-soft: #e98a5a;
    --page: #ffffff;
  }
  html, body {
    margin: 0;
    padding: 0;
    width: 1174px;
    height: 1200px;
    overflow: hidden;
    background: var(--page);
  }
  .label {
    display: block;
    width: 1174px;
    height: 1200px;
  }
  .brand-name {
    font-family: "Oswald", sans-serif;
    font-weight: 700;
    font-size: 124px;
    fill: var(--ink);
  }
  .tagline {
    font-family: "Oswald", sans-serif;
    font-weight: 400;
    font-size: 38px;
    fill: var(--ink);
  }
  .flavour-name {
    font-family: "Oswald", sans-serif;
    font-weight: 300;
    font-size: 42px;
    letter-spacing: 3px;
    fill: var(--ink);
  }
  .ink-line { stroke: var(--ink); fill: none; stroke-linecap: round; }
</style>
</head>
<body>
<svg class="label" viewBox="0 0 1276 1304" preserveAspectRatio="none" xmlns="http://www.w3.org/2000/svg">
  <defs>
    <clipPath id="label-inner">
      <path d="M28,210 Q28,150 88,150 H380 C450,150 490,38 638,38 C786,38 826,150 896,150 H1188 Q1248,150 1248,210 V1225 Q1248,1282 1190,1282 H86 Q28,1282 28,1225 Z"/>
    </clipPath>
    <radialGradient id="artwork-tone" cx="50%" cy="50%" r="60%">
      <stop offset="0" stop-color="var(--art-red)"/>
      <stop offset="1" stop-color="var(--art-soft)"/>
    </radialGradient>
  </defs>

  <!-- label shape -->
  <path class="label-outer" fill="var(--label-cream)"
        d="M0,190 Q0,122 68,122 H360 C430,122 470,0 638,0 C806,0 846,122 916,122 H1208 Q1276,122 1276,190 V1236 Q1276,1304 1208,1304 H68 Q0,1304 0,1236 Z"/>

  <g clip-path="url(#label-inner)">
    <rect class="upper-field" x="0" y="0" width="1276" height="1304" fill="var(--label-yellow)"/>
    <path class="wave-shadow" fill="var(--wave-shadow)"
          d="M0,1040 C160,1030 300,1010 420,950 C520,900 570,870 640,830 C740,780 820,745 900,740 C1010,730 1060,620 1100,510 C1140,410 1200,360 1276,290 V1304 H0 Z"/>
    <path class="lower-field" fill="var(--label-cream)"
          d="M0,1070 C160,1060 300,1040 420,980 C520,930 570,900 640,860 C740,810 820,775 900,770 C1020,760 1075,650 1115,540 C1155,440 1210,395 1276,330 V1304 H0 Z"/>
  </g>

  <path class="label-frame" fill="none" stroke="var(--frame-gold)" stroke-width="12"
        d="M28,210 Q28,150 88,150 H380 C450,150 490,38 638,38 C786,38 826,150 896,150 H1188 Q1248,150 1248,210 V1225 Q1248,1282 1190,1282 H86 Q28,1282 28,1225 Z"/>

  <!-- badge -->
  <circle class="badge" cx="638" cy="123" r="64" fill="var(--ink)" stroke="var(--label-yellow)" stroke-width="6"/>

  <!-- brand block -->
  <path class="ink-line" stroke-width="3" d="M215,272 Q400,238 590,229"/>
  <path class="ink-line" stroke-width="3" d="M695,233 Q890,240 1070,276"/>
  <path class="ink-line" stroke-width="3" d="M215,462 Q400,425 590,415"/>
  <path class="ink-line" stroke-width="3" d="M695,420 Q890,428 1070,463"/>

  <path id="brand-arc" d="M205,425 Q640,305 1075,420" fill="none"/>
  <text class="brand-name">
    <textPath href="#brand-arc" startOffset="0" textLength="865" lengthAdjust="spacing">WALDHORN</textPath>
  </text>

  <path id="tagline-arc" d="M418,487 Q646,462 876,487" fill="none"/>
  <text class="tagline">
    <textPath href="#tagline-arc" startOffset="0" textLength="457" lengthAdjust="spacing">Brauhandwerk &amp; Leidenschaft</textPath>
  </text>

  <!-- fruit artwork area -->
  <rect class="fruit-artwork" role="img" aria-label="Photograph of a red apple with a green leaf"
        x="395" y="555" width="490" height="445" rx="24" fill="url(#artwork-tone)" opacity="0.85"/>

  <!-- flavour -->
  <line class="ink-line" stroke-width="2" x1="360" y1="1136" x2="560" y2="1136"/>
  <line class="ink-line" stroke-width="2" x1="710" y1="1136" x2="910" y2="1136"/>
  <text class="flavour-name" x="638" y="1151" text-anchor="middle">Apple</text>
</svg>
</body>
</html>
```